Process Roadmap for Interior Design Firm

We are looking to ramp up the design appeal of our current process roadmap to be very visually interesting, while staying informative and descriptive about our process.

Target Market(s)

In-house Clients

Industry/Entity Type

Interior Design Firm focused on sustainable and holistic design.

Other font styles liked:
• raleway

Requirements
Must have
• 1.) it would be nice if the graphic provided a more clear indication of the “journey” from one step to the next, so that there was a clear sense of the progression (such that we are directing the viewer) 2.). We would want it to fit on an 8.5”x11” page (the page could be horizontal when we have the Steady Pathway formatted out with the testimonials) (in addition to the testimonials, we may also want to have the detailed descriptions of each step of the process presented below the graphic, so that the graphic is cleaner) 3.) ideally the graphic is clear and simple enough to also be used on our Bi-Weekly Client Updates, which will be typed updates for clients re their project budgets, schedule and scope. The Steady Pathway graphic (without all the testimonials) would be at the end of the update, and would fit on the page horizontally at the bottom, perhaps in a space which is 7.5”w x 4”h or so.
Should not have
• bold or bright colors. Natural neutrals are preferred, such as the ones featured on the provided graphic.

```html
<!DOCTYPE html>
<html lang="en">
<head>
<meta charset="utf-8">
<title>HVL Steady Pathway</title>
<link rel="stylesheet" href="https://fonts.googleapis.com/css2?family=Montserrat:wght@600&family=Raleway:wght@500&family=Arimo&display=swap">
<style>
  :root{
    --gold:#BD974E;
    --sand:#DFD1AC;
    --label:#C8B287;
    --paper:#FFFFFF;
    --pattern-a:#F6F0E2;
    --pattern-b:#E6DBBD;
  }
  html,body{margin:0;padding:0;width:1200px;height:927px;overflow:hidden;background:var(--paper);}
  .page{position:relative;width:2184px;height:1688px;transform:scale(0.549451);transform-origin:0 0;background:var(--paper);}
  .art{position:absolute;left:0;top:0;width:2184px;height:1688px;}
  .title{position:absolute;left:678px;top:77px;height:145px;line-height:145px;margin:0;
    font-family:"Montserrat",sans-serif;font-weight:600;font-size:106px;letter-spacing:4px;color:var(--paper);white-space:nowrap;}
  .step-label{position:absolute;width:287px;height:48px;line-height:50px;text-align:center;
    font-family:"Raleway",sans-serif;font-weight:500;font-size:27px;letter-spacing:3px;color:var(--paper);}
  .step-text{position:absolute;width:330px;text-align:center;color:var(--gold);
    font-family:"Arimo",sans-serif;font-size:26px;line-height:29px;}
  .step-text p{margin:0 0 29px;}
  .step-text p:last-child{margin-bottom:0;}
  .testimonials-title{position:absolute;left:773px;top:1230px;width:637px;height:80px;line-height:82px;text-align:center;margin:0;
    font-family:"Montserrat",sans-serif;font-weight:600;font-size:50px;letter-spacing:14px;color:var(--paper);}
</style>
</head>
<body>
<div class="page">
  <svg class="art" viewBox="0 0 2184 1688" xmlns="http://www.w3.org/2000/svg">
    <defs>
      <linearGradient id="patternTone" x1="0" y1="0" x2="1" y2="1">
        <stop offset="0" stop-color="var(--pattern-a)"/>
        <stop offset="1" stop-color="var(--pattern-b)"/>
      </linearGradient>
    </defs>

    <rect class="pattern-panel" x="0" y="0" width="400" height="1240" fill="url(#patternTone)" role="img" aria-label="Decorative chevron line pattern in soft sand tones"/>

    <!-- header bars -->
    <rect x="629" y="46" width="1555" height="8" fill="var(--sand)"/>
    <rect x="674" y="180" width="1510" height="86" fill="var(--sand)"/>
    <rect x="629" y="77" width="1555" height="145" fill="var(--gold)"/>

    <!-- guide lines -->
    <rect x="1134" y="379" width="1050" height="8" fill="var(--sand)"/>
    <rect x="1331" y="1049" width="853" height="8" fill="var(--sand)"/>
    <rect x="752" y="1106" width="1432" height="8" fill="var(--sand)"/>

    <!-- top row steps -->
    <g class="step-frame">
      <path d="M258 337 L81 514 L81 715 L258 892 L435 715 L435 514 Z" fill="var(--paper)" stroke="var(--paper)" stroke-width="50" stroke-linejoin="miter"/>
      <path d="M258 337 L81 514 L81 715 L258 892 L435 715 L435 514 Z" fill="var(--paper)" stroke="var(--gold)" stroke-width="20"/>
      <rect x="114" y="415" width="287" height="48" fill="var(--label)" stroke="var(--paper)" stroke-width="22"/>
    </g>
    <g class="step-frame">
      <path d="M814 337 L637 514 L637 715 L814 892 L991 715 L991 514 Z" fill="var(--paper)" stroke="var(--paper)" stroke-width="50"/>
      <path d="M814 337 L637 514 L637 715 L814 892 L991 715 L991 514 Z" fill="var(--paper)" stroke="var(--gold)" stroke-width="20"/>
      <rect x="670" y="415" width="287" height="48" fill="var(--label)" stroke="var(--paper)" stroke-width="22"/>
    </g>
    <g class="step-frame">
      <path d="M1368 337 L1191 514 L1191 715 L1368 892 L1545 715 L1545 514 Z" fill="var(--paper)" stroke="var(--paper)" stroke-width="50"/>
      <path d="M1368 337 L1191 514 L1191 715 L1368 892 L1545 715 L1545 514 Z" fill="var(--paper)" stroke="var(--gold)" stroke-width="20"/>
      <rect x="1224" y="415" width="287" height="48" fill="var(--label)" stroke="var(--paper)" stroke-width="22"/>
    </g>
    <g class="step-frame">
      <path d="M1924 337 L1747 514 L1747 715 L1924 892 L2101 715 L2101 514 Z" fill="var(--paper)" stroke="var(--paper)" stroke-width="50"/>
      <path d="M1924 337 L1747 514 L1747 715 L1924 892 L2101 715 L2101 514 Z" fill="var(--paper)" stroke="var(--gold)" stroke-width="20"/>
      <rect x="1781" y="415" width="287" height="48" fill="var(--label)" stroke="var(--paper)" stroke-width="22"/>
    </g>

    <!-- bottom row steps -->
    <g class="step-frame">
      <path d="M537 617 L360 794 L360 995 L537 1172 L714 995 L714 794 Z" fill="var(--paper)" stroke="var(--paper)" stroke-width="50"/>
      <path d="M537 617 L360 794 L360 995 L537 1172 L714 995 L714 794 Z" fill="var(--paper)" stroke="var(--gold)" stroke-width="20"/>
      <rect x="393" y="725" width="287" height="48" fill="var(--label)" stroke="var(--paper)" stroke-width="22"/>
    </g>
    <g class="step-frame">
      <path d="M1091 617 L914 794 L914 995 L1091 1172 L1268 995 L1268 794 Z" fill="var(--paper)" stroke="var(--paper)" stroke-width="50"/>
      <path d="M1091 617 L914 794 L914 995 L1091 1172 L1268 995 L1268 794 Z" fill="var(--paper)" stroke="var(--gold)" stroke-width="20"/>
      <rect x="948" y="725" width="287" height="48" fill="var(--label)" stroke="var(--paper)" stroke-width="22"/>
    </g>
    <g class="step-frame">
      <path d="M1646 617 L1469 794 L1469 995 L1646 1172 L1823 995 L1823 794 Z" fill="var(--paper)" stroke="var(--paper)" stroke-width="50"/>
      <path d="M1646 617 L1469 794 L1469 995 L1646 1172 L1823 995 L1823 794 Z" fill="var(--paper)" stroke="var(--gold)" stroke-width="20"/>
      <rect x="1503" y="725" width="287" height="48" fill="var(--label)" stroke="var(--paper)" stroke-width="22"/>
    </g>

    <!-- testimonials band -->
    <rect x="0" y="1248" width="2184" height="440" fill="var(--sand)"/>
    <rect x="773" y="1230" width="637" height="80" rx="40" fill="var(--gold)"/>

    <g class="testimonial-bubble">
      <path d="M145 1362 H468 a60 60 0 0 1 60 60 V1548 a60 60 0 0 1 -60 60 H234 V1636 a12 12 0 0 1 -22 6 L190 1608 H145 a60 60 0 0 1 -60 -60 V1422 a60 60 0 0 1 60 -60 Z" fill="var(--paper)"/>
      <path d="M133 1350 H450 a60 60 0 0 1 60 60 V1530 a60 60 0 0 1 -60 60 H216 V1622 a8 8 0 0 1 -14 4 L175 1590 H133 a60 60 0 0 1 -60 -60 V1410 a60 60 0 0 1 60 -60 Z" fill="none" stroke="var(--gold)" stroke-width="5"/>
    </g>
    <g class="testimonial-bubble" transform="translate(523 0)">
      <path d="M145 1362 H468 a60 60 0 0 1 60 60 V1548 a60 60 0 0 1 -60 60 H234 V1636 a12 12 0 0 1 -22 6 L190 1608 H145 a60 60 0 0 1 -60 -60 V1422 a60 60 0 0 1 60 -60 Z" fill="var(--paper)"/>
      <path d="M133 1350 H450 a60 60 0 0 1 60 60 V1530 a60 60 0 0 1 -60 60 H216 V1622 a8 8 0 0 1 -14 4 L175 1590 H133 a60 60 0 0 1 -60 -60 V1410 a60 60 0 0 1 60 -60 Z" fill="none" stroke="var(--gold)" stroke-width="5"/>
    </g>
    <g class="testimonial-bubble" transform="translate(1073 0)">
      <path d="M145 1362 H468 a60 60 0 0 1 60 60 V1548 a60 60 0 0 1 -60 60 H234 V1636 a12 12 0 0 1 -22 6 L190 1608 H145 a60 60 0 0 1 -60 -60 V1422 a60 60 0 0 1 60 -60 Z" fill="var(--paper)"/>
      <path d="M133 1350 H450 a60 60 0 0 1 60 60 V1530 a60 60 0 0 1 -60 60 H216 V1622 a8 8 0 0 1 -14 4 L175 1590 H133 a60 60 0 0 1 -60 -60 V1410 a60 60 0 0 1 60 -60 Z" fill="none" stroke="var(--gold)" stroke-width="5"/>
    </g>
    <g class="testimonial-bubble" transform="translate(1596 0)">
      <path d="M145 1362 H468 a60 60 0 0 1 60 60 V1548 a60 60 0 0 1 -60 60 H234 V1636 a12 12 0 0 1 -22 6 L190 1608 H145 a60 60 0 0 1 -60 -60 V1422 a60 60 0 0 1 60 -60 Z" fill="var(--paper)"/>
      <path d="M133 1350 H450 a60 60 0 0 1 60 60 V1530 a60 60 0 0 1 -60 60 H216 V1622 a8 8 0 0 1 -14 4 L175 1590 H133 a60 60 0 0 1 -60 -60 V1410 a60 60 0 0 1 60 -60 Z" fill="none" stroke="var(--gold)" stroke-width="5"/>
    </g>
  </svg>

  <h1 class="title">HVL Steady Pathway</h1>

  <div class="step-label" style="left:114px;top:415px;">LISTENING</div>
  <div class="step-label" style="left:670px;top:415px;">PLANNING</div>
  <div class="step-label" style="left:1224px;top:415px;">MANAGING</div>
  <div class="step-label" style="left:1781px;top:415px;">COMPLETING</div>
  <div class="step-label" style="left:393px;top:725px;">VISIONING</div>
  <div class="step-label" style="left:948px;top:725px;">DESIGNING</div>
  <div class="step-label" style="left:1503px;top:725px;">INSTALLING</div>

  <div class="step-text" style="left:93px;top:553px;">
    <p>Listening to our clients, their land, and their home.</p>
    <p>Identifying their needs, challenges, wishes, and dreams.</p>
  </div>
  <div class="step-text" style="left:649px;top:500px;">
    <p>Turning our client’s vision into a clearly defined scope, budget, and timeline.</p>
    <p>Mapping out the steps for making their dream a reality.</p>
    <p>Setting a meeting schedule from start to finish.</p>
  </div>
  <div class="step-text" style="left:1203px;top:526px;">
    <p>Coordinating with clients, builders, architects, and vendors to ensure that the design is executed with excellence, and the furnishings are on-time and on budget.</p>
  </div>
  <div class="step-text" style="left:1759px;top:496px;">
    <p>Fixing any issues or defects.</p>
    <p>Follow up on all remaining items.</p>
    <p>Completing the final finishing touches to our client’s full and total satisfaction.</p>
  </div>
  <div class="step-text" style="left:372px;top:818px;">
    <p>Facilitating a guided visioning process to clarify the deepest intention, true purpose, and highest potential for their home and their future within it.</p>
  </div>
  <div class="step-text" style="left:921px;top:813px;width:340px;">
    <p>Following the schedule through the design phases from initial design concepts, technical drawings and details, and the selection of all finishes, fixtures, and surnishings.</p>
  </div>
  <div class="step-text" style="left:1481px;top:781px;">
    <p>Overseeing the inspection, installation, and arrangement of all furnishings, lightning, artwork, and decorative items</p>
    <p>Taking care of every last detail.</p>
  </div>

  <h2 class="testimonials-title">TESTIMONIALS</h2>
</div>
</body>
</html>
```